New Business Card Design Project

I would like to purchase a customized version of a design you have previously submitted - https://www.artflocksite.com.au/design/58210937

We meed a buisness card design i have attached my logo this card needs to have

Address : 14 Brambleton Road Carrowdale North 3091
Phone: 03 97142283
Email sales@tarvickautotrade.com.au
website: tarwickautotrade.com.au
and at the back a review us on findly and review us on chatterly (small image of that)

i like the design attached but would like other vehciles such as Veltrano KZR OSKA and Dorringhaus vehicles as were a australian dealer

Thanks

Target Market(s)

car sales

Industry/Entity Type

Automotive

Contact Information for Business Card

Address, name , logo, website number and review us on the back

Colors

Designer to choose only greyscale colors for use in the design.

Requirements
Must have
• Address : 14 Brambleton Road Carrowdale North 3091 Phone: 03 97142283 Email sales@tarvickautotrade.com.au
Nice to have
• Black background cars as a background Oska, Kellard Veltranno , KZR in a lineup

```html
<!DOCTYPE html>
<html lang="en">
<head>
<meta charset="utf-8">
<title>Tarwick Auto Trade – Business Card</title>
<link href="https://fonts.googleapis.com/css2?family=Poppins:wght@400;500;600&display=swap" rel="stylesheet">
<style>
  :root {
    --backdrop: #2b2e30;
    --card: #262626;
    --card-edge: #1c1c1c;
    --ink: #ffffff;
    --ink-soft: #d9d9d9;
    --emboss: #141414;
    --emboss-light: #383838;
    --accent: #e0161e;
    --star: #f2b100;
  }
  * { margin: 0; padding: 0; box-sizing: border-box; }
  html, body { width: 1200px; height: 939px; overflow: hidden; background: var(--backdrop); }
  body { position: relative; font-family: "Poppins", sans-serif; }

  .card {
    position: absolute;
    left: 260px;
    width: 680px;
    height: 390px;
    background: var(--card);
    border: 1px solid var(--card-edge);
    box-shadow: 0 12px 30px rgba(0,0,0,.45);
    overflow: hidden;
  }
  .card--back { top: 50px; }
  .card--front { top: 495px; }

  /* Back: embossed name */
  .emboss-mark {
    position: absolute;
    left: 0; right: 0; top: 160px;
    text-align: center;
  }
  .emboss-mark .brand-name {
    font-weight: 600;
    font-size: 34px;
    letter-spacing: 2px;
    text-transform: uppercase;
    color: var(--emboss);
    text-shadow: 0 1px 0 var(--emboss-light);
  }
  .emboss-mark .tagline {
    font-weight: 400;
    font-size: 15px;
    letter-spacing: 1px;
    color: var(--emboss);
    text-shadow: 0 1px 0 var(--emboss-light);
    margin-top: 2px;
  }

  /* Front */
  .front-mark {
    position: absolute;
    left: 150px; top: 42px;
    width: 380px;
    text-align: center;
  }
  .front-mark .brand-name {
    font-weight: 600;
    font-size: 26px;
    letter-spacing: 1.5px;
    text-transform: uppercase;
    color: var(--ink);
  }
  .front-mark .tagline {
    font-weight: 400;
    font-size: 13px;
    letter-spacing: 1px;
    color: var(--ink-soft);
    margin-top: 2px;
  }

  .car { position: absolute; border-radius: 40% 40% 12% 12% / 55% 55% 14% 14%; }
  .car--kzr { left: 140px; top: 190px; width: 150px; height: 80px;
    background: linear-gradient(180deg, #4a4a5c, #2b2b36); }
  .car--veltrano { left: 295px; top: 162px; width: 135px; height: 70px;
    background: linear-gradient(180deg, #f2f2f2, #bdbdbd); }
  .car--oska { left: 432px; top: 132px; width: 100px; height: 58px;
    background: linear-gradient(180deg, #cfd0d3, #8d8f94); }
  .car--kellard { left: 545px; top: 92px; width: 110px; height: 62px;
    background: linear-gradient(180deg, #4b3f8f, #241e52); }

  .contact {
    position: absolute;
    left: 90px; top: 284px;
    list-style: none;
    color: var(--ink);
    font-size: 15px;
    line-height: 22px;
  }
  .contact li { display: flex; align-items: center; gap: 8px; }
  .contact svg { width: 13px; height: 13px; fill: var(--accent); flex: none; }
  .contact .phone { letter-spacing: 3px; }

  .reviews {
    position: absolute;
    right: 20px; top: 172px;
    width: 110px;
    text-align: center;
    color: var(--ink);
  }
  .review { margin-bottom: 12px; }
  .review .label { font-size: 8px; font-weight: 600; text-transform: uppercase; letter-spacing: .5px; }
  .review .site { font-size: 22px; font-weight: 600; line-height: 1.1; }
  .review .stars { color: var(--star); font-size: 12px; letter-spacing: 2px; }
</style>
</head>
<body>

  <section class="card card--back" aria-label="Card back">
    <div class="emboss-mark">
      <div class="brand-name">Tarwick Auto Trade</div>
      <div class="tagline">Driving Your Plans Forward</div>
    </div>
  </section>

  <section class="card card--front" aria-label="Card front">
    <div class="front-mark">
      <div class="brand-name">Tarwick Auto Trade</div>
      <div class="tagline">Driving Your Plans Forward</div>
    </div>

    <div class="lineup">
      <div class="car car--kzr" role="img" aria-label="Photo of a dark grey KZR sedan"></div>
      <div class="car car--veltrano" role="img" aria-label="Photo of a white Veltrano coupe"></div>
      <div class="car car--oska" role="img" aria-label="Photo of a silver Oska sedan"></div>
      <div class="car car--kellard" role="img" aria-label="Photo of a purple Kellard sports saloon"></div>
    </div>

    <ul class="contact">
      <li><svg viewBox="0 0 24 24"><path d="M6.6 10.8a15 15 0 0 0 6.6 6.6l2.2-2.2c.3-.3.7-.4 1-.2 1.1.4 2.3.6 3.6.6.6 0 1 .4 1 1V20c0 .6-.4 1-1 1A17 17 0 0 1 3 4c0-.6.4-1 1-1h3.5c.6 0 1 .4 1 1 0 1.3.2 2.5.6 3.6.1.3 0 .7-.2 1z"/></svg><span class="phone">03 97142283</span></li>
      <li><svg viewBox="0 0 24 24"><path d="M2 5h20v14H2zm2 2v.5l8 5 8-5V7l-8 5z"/></svg><span>sales@tarvickautotrade.com.au</span></li>
      <li><svg viewBox="0 0 24 24"><path d="M12 2a10 10 0 1 0 0 20 10 10 0 0 0 0-20zm0 2c.8 1.2 1.5 2.5 1.9 4h-3.8c.4-1.5 1.1-2.8 1.9-4zM4.3 14a8 8 0 0 1 0-4h3.4a16 16 0 0 0 0 4zm5.4 0a15 15 0 0 1 0-4h4.6a15 15 0 0 1 0 4zm6.6 0a16 16 0 0 0 0-4h3.4a8 8 0 0 1 0 4zM12 20c-.8-1.2-1.5-2.5-1.9-4h3.8c-.4 1.5-1.1 2.8-1.9 4z"/></svg><span>tarwickautotrade.com.au</span></li>
      <li><svg viewBox="0 0 24 24"><path d="M12 2a7 7 0 0 0-7 7c0 5.2 7 13 7 13s7-7.8 7-13a7 7 0 0 0-7-7zm0 9.5a2.5 2.5 0 1 1 0-5 2.5 2.5 0 0 1 0 5z"/></svg><span>14 Brambleton Road Carrowdale North 3091</span></li>
    </ul>

    <div class="reviews">
      <div class="review">
        <div class="label">Review us on</div>
        <div class="site">findly</div>
        <div class="stars">★★★★★</div>
      </div>
      <div class="review">
        <div class="site">chatterly</div>
        <div class="stars">★★★★★</div>
      </div>
    </div>
  </section>

</body>
</html>
```